VaultMeridan Business Card Re-Design

VaultMeridan is a specialized information security company that applies its proven methodology of security Assessment, Development, Integration and Training (A-D-I-T) to provide cyber security services in the areas of Data Protection, Network Defense and Compliance. We need the current business card re-designed to properly scale the fonts and possibly rearranging some elements (icons, lettering, etc.) to make the card more appealing to the eye. The card should have the logo that is on the web site (www.vaultmeridan-example.com). We would like ideas for both a black card (black background) and a white card (white background). We prefer rounded corners to help the card stand out but are open to all ideas. FYI: VaultMeridan's slogan is "...your security is our business".

Target Market(s)

#1 US Government Contracting Companies, #2 Commercial Companies, #3 Gen. Public.

Industry/Entity Type

Business

Contact Information for Business Card

See Description; open to the use of different fonts.

Font styles to use
Sans Serif

Colors
000000
ec1f27
ffffff

Requirements
Must have
• Company logo on web site, rounded corners, list of company offerings on the back of the card.
Nice to have
• Icons
Should not have
• none

```html
<!DOCTYPE html>
<html lang="en">
<head>
<meta charset="utf-8">
<title>VaultMeridan Business Card</title>
<link rel="stylesheet" href="https://fonts.googleapis.com/css2?family=Jura:wght@400;500;600&display=swap">
<style>
  :root {
    --ink: #000000;
    --signal-red: #ec1f27;
    --paper: #ffffff;
    --page: #ffffff;
    --card-shadow: rgba(0, 0, 0, 0.35);
  }
  * { margin: 0; padding: 0; box-sizing: border-box; }
  html, body {
    width: 1200px;
    height: 900px;
    overflow: hidden;
    background: var(--page);
  }
  body {
    position: relative;
    font-family: "Jura", "Segoe UI", sans-serif;
    color: var(--paper);
  }
  .business-card {
    position: absolute;
    left: 113px;
    top: 170px;
    width: 960px;
    height: 550px;
    background: var(--ink);
    border-radius: 34px;
    box-shadow: 6px 8px 8px var(--card-shadow);
  }
  .brand {
    position: absolute;
    left: 56px;
    top: 100px;
    display: flex;
    align-items: center;
    gap: 16px;
  }
  .brand-mark {
    width: 28px;
    height: 28px;
    background: var(--signal-red);
  }
  .brand-name {
    font-size: 46px;
    font-weight: 500;
    letter-spacing: 5px;
    color: var(--paper);
    line-height: 1;
  }
  .divider {
    position: absolute;
    left: 534px;
    top: 67px;
  }
  .person {
    position: absolute;
    right: 70px;
    top: 62px;
    text-align: right;
  }
  .person-name {
    font-size: 42px;
    font-weight: 500;
    line-height: 1.1;
    letter-spacing: 0.5px;
  }
  .person-name .surname { color: var(--signal-red); }
  .person-role {
    margin-top: 6px;
    font-size: 28px;
    font-weight: 500;
    line-height: 1.1;
  }
  .person-role .accent { color: var(--signal-red); }
  .person-credentials {
    margin-top: 14px;
    font-size: 19px;
    font-weight: 500;
    color: var(--signal-red);
    letter-spacing: 0.5px;
  }
  .contact-list {
    position: absolute;
    left: 200px;
    top: 278px;
    list-style: none;
  }
  .contact-item {
    display: flex;
    align-items: center;
    height: 39px;
    font-size: 20px;
    font-weight: 500;
    letter-spacing: 0.3px;
  }
  .contact-icon {
    width: 22px;
    height: 22px;
    margin-right: 12px;
    flex: none;
  }
  .contact-item .gap { margin-left: 20px; }
  .company-address {
    position: absolute;
    left: 0;
    right: 0;
    top: 492px;
    text-align: center;
    font-size: 21px;
    font-weight: 500;
    letter-spacing: 0.4px;
  }
</style>
</head>
<body>
  <div class="business-card">
    <div class="brand">
      <span class="brand-mark"></span>
      <span class="brand-name">VAULTMERIDAN</span>
    </div>

    <svg class="divider" width="72" height="128" viewBox="0 0 72 128" aria-hidden="true">
      <line x1="2" y1="2" x2="70" y2="126" stroke="var(--signal-red)" stroke-width="1.5"/>
    </svg>

    <div class="person">
      <p class="person-name">Marcus <span class="surname">Hale</span></p>
      <p class="person-role">President<span class="accent">\CEO</span></p>
      <p class="person-credentials">CSDP, C\NA</p>
    </div>

    <ul class="contact-list">
      <li class="contact-item">
        <svg class="contact-icon" viewBox="0 0 24 24" aria-hidden="true">
          <path d="M8 3c-1.5 0-3 1.6-3 4 0 5 4 12 9 14 2 .8 3.5-.4 4-1.5l-3-3.5-2.2 1.2C10.8 16 9 13 8.6 10.6l2.1-1.3L9.5 4.5C9.2 3.6 8.7 3 8 3z" fill="var(--signal-red)"/>
        </svg>
        <span>240.555.0142</span>
        <svg class="contact-icon gap" viewBox="0 0 24 24" aria-hidden="true">
          <rect x="6.5" y="2" width="11" height="20" rx="2" fill="none" stroke="var(--signal-red)" stroke-width="2.2"/>
          <rect x="10" y="18" width="4" height="1.6" fill="var(--signal-red)"/>
        </svg>
        <span>301.555.0187</span>
      </li>
      <li class="contact-item">
        <svg class="contact-icon" viewBox="0 0 24 24" aria-hidden="true">
          <rect x="2" y="5" width="20" height="14" fill="var(--signal-red)"/>
          <path d="M2 5l10 8 10-8" fill="none" stroke="var(--ink)" stroke-width="1.6"/>
        </svg>
        <span>info@vaultmeridan-example.com \ mhale@vaultmeridan-example.com</span>
      </li>
      <li class="contact-item">
        <svg class="contact-icon" viewBox="0 0 24 24" aria-hidden="true">
          <circle cx="12" cy="12" r="9.5" fill="var(--signal-red)"/>
          <g fill="none" stroke="var(--ink)" stroke-width="1.3">
            <ellipse cx="12" cy="12" rx="4" ry="9.5"/>
            <line x1="2.5" y1="12" x2="21.5" y2="12"/>
            <line x1="12" y1="2.5" x2="12" y2="21.5"/>
            <path d="M4 7.5h16M4 16.5h16"/>
          </g>
        </svg>
        <span>www.vaultmeridan-example.com</span>
      </li>
    </ul>

    <p class="company-address">VaultMeridan, Inc. \ 4120 Harbor Ridge Rd. Suite 210 \ Larkfield, Westmora 30917</p>
  </div>
</body>
</html>
```